Business card design needed

Family General Practitioner/ Family Physician.
Logo is the logo of the Imperial Guild of Community Clinicians Oceania
http://pkvtm.lorimar.example/PictureGallery/logos/pages/IGCCO%20logo_jpg.htm

Reason: Just a bit more time to make changes and the weekend for me to look at things closely and to choose. Thanks, Ulan

Thanks for all the submissions. So many of them are really works of art. Not one of them are not good. The ones that I am eliminating are the ones that I think are not suitable for me personally only, and because if I don't, it makes it very difficult to decide as many of you are also sending me slight variations of a card. I have just decided to choose a second place card too. Can't thank you all enough. Good luck, Ulan. P.S - Working today till 10 pm as the card says :-), so probably won't be able to give a feedback till late Saturday night or Sunday morning here in Sydney, Australia. 

Reason: Just added a second place to the budget and realised that Australia is ahead of the rest of the world in the time zone (only :-) - don't want to offend anyone or start a debate!! ) , so Monday deadline will mean it will be a weekend for the rest of the world. Just wanted to give everyone more time to submit their best, especially since I will be picking a second card too. Can't thank everyone enough for the submissions. P.S - Not keen on photos on the card.

Business

Contact Information for Business Card

Dr. Ulan Pereira M.B.B.S., F.I.G.C.C.O
Family General Practitioner
Address, timings, phone and fax number on the back.

Requirements
Must have
• Timings
Mon 7 am - 7 pm
Tues 7 am - 12 pm
Wed 7 am - 10 pm
Thurs 7 am - 12 pm
Fri 7 am - 8 pm
Sat 8 am - 10 pm
Sun - Off

```html
<!DOCTYPE html>
<html lang="en">
<head>
<meta charset="utf-8">
<title>Dr. Ulan Pereira – Business Card</title>
<link rel="stylesheet" href="https://fonts.googleapis.com/css2?family=Michroma&family=Open+Sans:wght@400;600;700&display=swap">
<style>
  :root {
    --page-bg: #2a2a2a;
    --gold-light: #f2ab1e;
    --gold-mid: #b57e14;
    --gold-dark: #5e420c;
    --card-white: #f3f5f7;
    --accent-red: #d0202a;
    --deep-red: #8a1015;
    --rule-gold: #d99a1a;
    --text-white: #ffffff;
  }
  * { box-sizing: border-box; margin: 0; padding: 0; }
  html, body { width: 1200px; height: 900px; overflow: hidden; }
  body {
    background: var(--page-bg);
    font-family: "Open Sans", Arial, sans-serif;
    position: relative;
  }
  .card {
    position: absolute;
    left: 280px;
    width: 640px;
    height: 366px;
    overflow: hidden;
    box-shadow: 0 10px 30px rgba(0,0,0,0.5);
  }

  /* Back of card */
  .card-back { top: 52px; background: var(--card-white); }
  .hours {
    position: absolute;
    left: 48px;
    top: 36px;
    width: 300px;
    list-style: none;
    font-family: "Open Sans", Arial, sans-serif;
    font-weight: 700;
    font-size: 15px;
    color: var(--accent-red);
  }
  .hours li {
    display: flex;
    align-items: center;
    height: 23px;
  }
  .hours .day { width: 92px; }
  .hours .leader {
    flex: 1;
    height: 1px;
    background: var(--rule-gold);
    margin: 0 8px;
  }
  .hours .time { width: 100px; }
  .back-band {
    position: absolute;
    left: 0; right: 0; bottom: 0;
    height: 152px;
    background: radial-gradient(ellipse at 70% 10%, var(--gold-light) 0%, var(--gold-mid) 45%, var(--gold-dark) 100%);
    border-top: 4px solid var(--card-white);
    box-shadow: 0 -2px 0 var(--gold-mid);
  }
  .address {
    position: absolute;
    left: 48px;
    top: 34px;
    color: var(--text-white);
    font-size: 15px;
    line-height: 22px;
  }
  .contact {
    position: absolute;
    left: 48px;
    top: 92px;
    font-size: 17px;
    font-weight: 700;
    color: var(--text-white);
  }
  .contact .number { color: var(--accent-red); margin-right: 18px; }

  /* Front of card */
  .card-front {
    top: 482px;
    background: radial-gradient(ellipse at 50% 42%, var(--gold-light) 0%, var(--gold-mid) 40%, var(--gold-dark) 100%);
    text-align: center;
  }
  .org-mark {
    position: absolute;
    left: 0; right: 0;
    top: 64px;
    display: flex;
    justify-content: center;
    align-items: center;
    gap: 10px;
    font-family: "Michroma", Arial, sans-serif;
    font-size: 22px;
    color: var(--deep-red);
  }
  .org-mark svg { display: block; }
  .doctor-name {
    position: absolute;
    left: 0; right: 0;
    top: 160px;
    font-family: "Michroma", Arial, sans-serif;
    font-size: 36px;
    letter-spacing: -1px;
    color: var(--accent-red);
  }
  .credentials {
    position: absolute;
    left: 0; right: 0;
    top: 212px;
    font-weight: 700;
    font-size: 15px;
    letter-spacing: 1px;
    color: var(--deep-red);
  }
  .role {
    position: absolute;
    left: 0; right: 0;
    top: 246px;
    font-size: 22px;
    color: var(--text-white);
  }
</style>
</head>
<body>

  <section class="card card-back">
    <ul class="hours">
      <li><span class="day">Monday</span><span class="leader"></span><span class="time">7 am - 7 pm</span></li>
      <li><span class="day">Tuesday</span><span class="leader"></span><span class="time">7 am - 12 pm</span></li>
      <li><span class="day">Wednesday</span><span class="leader"></span><span class="time">7 am - 10 pm</span></li>
      <li><span class="day">Thursday</span><span class="leader"></span><span class="time">7 am - 12 pm</span></li>
      <li><span class="day">Friday</span><span class="leader"></span><span class="time">7 am - 8 pm</span></li>
      <li><span class="day">Saturday</span><span class="leader"></span><span class="time">8 am - 10 pm</span></li>
      <li><span class="day">Sunday</span><span class="leader"></span><span class="time">Off</span></li>
    </ul>
    <div class="back-band">
      <p class="address">Upper Level, Harbour Walk, Ridgeview Shopping Centre<br>Maple Hill, NSW 2191</p>
      <p class="contact">P: <span class="number">02 7391 4620</span>F: <span class="number">02 7391 462</span></p>
    </div>
  </section>

  <section class="card card-front">
    <div class="org-mark">
      <svg width="22" height="22" viewBox="0 0 22 22" aria-hidden="true"><circle cx="11" cy="11" r="10" fill="var(--deep-red)"/></svg>
      <span>IGCCO</span>
    </div>
    <h1 class="doctor-name">DR. ULAN PEREIRA</h1>
    <p class="credentials">M.B.B.S., F.I.G.C.C.O</p>
    <p class="role">Family General Practitioner</p>
  </section>

</body>
</html>
```